Website Design for The Bootcrate

We have two Melbourne stores, The Bootcrate Factory Outlet in Ashburton and The Bootcrate Warehouse in Fairfield. We only stock well known brands and are the official outlet for Vennor and Softtrekkers. We sell our products at heavily discounted prices and

```html
<!DOCTYPE html>
<html lang="en">
<head>
<meta charset="utf-8">
<title>The Bootcrate – Locations</title>
<link href="https://fonts.googleapis.com/css2?family=Arvo:ital,wght@0,400;0,700;1,400&family=Shadows+Into+Light+Two&display=swap" rel="stylesheet">
<style>
  :root {
    --page-bg: #dcdcdc;
    --ink-dark: #1c1b1c;
    --panel: #ffffff;
    --sidebar: #f5f5f5;
    --tab-bg: #f3f3f3;
    --text: #333333;
    --accent: #c8202f;
    --photo-dark: #3a2c22;
    --photo-mid: #6b5a44;
    --map-light: #ede8de;
    --map-mid: #e2dccf;
  }
  * { box-sizing: border-box; margin: 0; padding: 0; }
  html, body { width: 1197px; height: 1200px; overflow: hidden; }
  body {
    position: relative;
    background: var(--page-bg);
    font-family: "Arvo", Georgia, serif;
    color: var(--text);
  }
  .side-band { position: absolute; left: 0; top: 31px; width: 47px; height: 1106px; background: var(--ink-dark); }
  .brand {
    position: absolute; left: 0; top: 31px; width: 317px; height: 59px;
    background: var(--ink-dark);
    display: flex; align-items: center; justify-content: center;
    color: #ffffff; font-size: 28px; font-weight: 400; letter-spacing: 1px;
  }
  .main-nav {
    position: absolute; left: 317px; top: 43px; width: 311px; height: 47px;
    background: var(--tab-bg);
    display: flex; align-items: center; padding-left: 24px;
    font-size: 20px; font-weight: 700;
  }
  .main-nav a { text-decoration: none; color: #666; padding-right: 18px; }
  .main-nav a + a { border-left: 1px solid #d6d6d6; padding-left: 18px; }
  .main-nav a.is-current { color: var(--accent); }
  .tagline {
    position: absolute; right: 66px; top: 35px;
    font-family: "Shadows Into Light Two", cursive;
    font-size: 17px; color: #666; white-space: nowrap;
    letter-spacing: -0.2px;
  }
  .panel { position: absolute; left: 47px; top: 90px; width: 1103px; height: 1047px; background: var(--panel); }
  .hours {
    position: absolute; left: 47px; top: 90px; width: 259px; height: 1047px;
    background: var(--sidebar); text-align: center; padding-top: 72px;
    font-size: 19px; line-height: 30px;
  }
  .hours h2 { font-size: 19px; font-weight: 700; color: #222; margin-bottom: 4px; }
  .hours .day { font-style: italic; }
  .hours .gap { height: 28px; }
  .store { position: absolute; left: 375px; width: 745px; }
  .store h1 { font-size: 29px; font-weight: 400; color: #333; }
  .store-media { display: flex; gap: 25px; margin-top: 27px; }
  .store-photo {
    width: 351px; height: 233px;
    background: linear-gradient(135deg, var(--photo-mid), var(--photo-dark) 60%, #2a211b);
  }
  .store-map {
    width: 365px; height: 236px;
    background: linear-gradient(160deg, var(--map-light), var(--map-mid));
  }
  .contact { margin-top: 14px; font-size: 19px; line-height: 35px; }
  .contact .label { text-decoration: underline; color: #444; }
  .contact .name { font-weight: 700; color: #222; }
  .contact .phone { font-family: Arial, Helvetica, sans-serif; color: #333; }
  .footer-brand {
    position: absolute; left: 0; top: 1137px; width: 317px; height: 63px;
    background: var(--ink-dark); color: #fff;
    font-family: Arial, Helvetica, sans-serif; font-size: 13px;
    display: flex; align-items: center; justify-content: center;
  }
  .footer-nav {
    position: absolute; left: 343px; top: 1161px; display: flex; gap: 26px;
    font-size: 13px; color: #555;
  }
  .like {
    position: absolute; left: 1051px; top: 1157px; display: flex; gap: 6px; align-items: center;
    font-family: Arial, Helvetica, sans-serif; font-size: 12px;
  }
  .like-button { display: flex; align-items: center; gap: 4px; border: 1px solid #c5c5c5; background: #f4f4f4; padding: 2px 5px; color: #3b5998; }
  .like-button i { width: 10px; height: 10px; background: #3b5998; display: block; }
  .like-count { border: 1px solid #c5c5c5; background: #fff; padding: 2px 6px; color: #333; }
</style>
</head>
<body>
  <div class="side-band"></div>
  <div class="brand">THE BOOTCRATE</div>
  <nav class="main-nav">
    <a href="#about">ABOUT US</a>
    <a href="#locations" class="is-current">LOCATIONS</a>
  </nav>
  <p class="tagline">The Official Factory outlet for Ashburton and Fairfield</p>

  <div class="panel"></div>
  <aside class="hours">
    <h2>Opening hours</h2>
    <p class="day">Monday to Friday:</p>
    <p>9am-5pm</p>
    <div class="gap"></div>
    <p class="day">Saturday:</p>
    <p>9am-4pm</p>
  </aside>

  <section class="store" style="top:153px">
    <h1>Ashburton Store</h1>
    <div class="store-media">
      <div class="store-photo" role="img" aria-label="Interior of the Ashburton store with shoe displays and a lounge"></div>
      <div class="store-map" role="img" aria-label="Street map showing the Ashburton store location"></div>
    </div>
    <div class="contact">
      <p><span class="label">Contact Detail</span>:</p>
      <p class="name">Ashburton Store</p>
      <p class="phone">Phone numbers: 555 010 234</p>
    </div>
  </section>

  <section class="store" style="top:635px">
    <h1>&nbsp;Fairfield Store</h1>
    <div class="store-media">
      <div class="store-photo" role="img" aria-label="Interior of the Fairfield store with shoe displays and a lounge"></div>
      <div class="store-map" role="img" aria-label="Street map showing the Fairfield store location"></div>
    </div>
    <div class="contact">
      <p><span class="label">Contact Detail</span>:</p>
      <p class="name">&nbsp;Fairfield Store</p>
      <p class="phone">Phone numbers: 555 010 234</p>
    </div>
  </section>

  <footer>
    <div class="footer-brand">© 2012 The Bootcrate</div>
    <nav class="footer-nav">
      <span>ABOUT US</span><span>LOCATIONS</span><span>CONTACT US</span>
    </nav>
    <div class="like">
      <span class="like-button"><i></i>Like</span>
      <span class="like-count">0</span>
    </div>
  </footer>
</body>
</html>
```